New corporate e-mail signature

We need a new e-mail signature for our company that is clean and professional. The requests are attached in a document.

Target Market(s)

CFO, CTO, Controllers, leaders, decision-makers.

Industry/Entity Type

Information Technology

Colors

Designer to choose colors to be used in the design.

Requirements
Must have
• See the PowerPoint document.
• - keep it as simple as possible.
• - same style as our new website design
• - It has to look good in all e-mail readers, and on all surfaces.
Nice to have
• - Please also attach 'best practise' for how to use the signature.
Should not have
• See the PowerPoint document. Use our color palette.
• - Do not include photo!

```html
<!DOCTYPE html>
<html lang="en">
<head>
<meta charset="UTF-8">
<title>Gainvault – E-mail Signature</title>
<link href="https://fonts.googleapis.com/css2?family=Montserrat:wght@400;600;700&display=swap" rel="stylesheet">
<style>
  :root {
    --page-bg: #f3f3f3;
    --card-bg: #ffffff;
    --accent: #26b5bf;
    --accent-light: #6dd0d4;
    --panel-top: #24b1bc;
    --panel-bottom: #0e4a78;
    --ink: #2b2b2b;
    --muted: #9a9a9a;
    --white: #ffffff;
  }
  * { margin: 0; padding: 0; box-sizing: border-box; }
  html, body {
    width: 1200px; height: 965px; overflow: hidden;
    background: var(--page-bg);
    font-family: "Montserrat", sans-serif;
  }
  .canvas { position: relative; width: 1200px; height: 965px; }
  .signature {
    position: absolute; left: 46px; width: 1107px; height: 324px;
    background: var(--card-bg);
    box-shadow: 0 14px 30px rgba(0,0,0,0.10);
    display: flex;
  }
  .signature--logo { top: 121px; }
  .signature--wordmark { top: 524px; }
  .contact { position: relative; width: 660px; }
  .contact__name {
    position: absolute; left: 184px; top: 88px;
    font-size: 32px; font-weight: 600; color: var(--accent); letter-spacing: 0.2px;
  }
  .contact__role {
    position: absolute; left: 185px; top: 128px;
    font-size: 20px; font-weight: 400; color: var(--muted); letter-spacing: 0.8px;
  }
  .contact__row {
    position: absolute; left: 186px; display: flex; align-items: center;
    font-size: 22px; color: var(--ink); letter-spacing: 0.4px;
  }
  .contact__row--email { top: 184px; }
  .contact__row--phone { top: 229px; }
  .contact__icon { width: 22px; height: 22px; margin-right: 20px; flex: none; }
  .divider { width: 10px; background: var(--accent-light); }
  .brand-panel {
    position: relative; flex: 1;
    background: linear-gradient(180deg, var(--panel-top) 0%, var(--panel-bottom) 100%);
    color: var(--white);
  }
  .brand-panel__name {
    position: absolute; left: 0; right: 0; text-align: center;
    font-weight: 700; color: var(--white);
  }
  .signature--logo .brand-panel__name { top: 120px; font-size: 36px; letter-spacing: -0.5px; }
  .signature--wordmark .brand-panel__name { top: 130px; font-size: 29px; letter-spacing: 0.5px; }
  .brand-panel__url {
    position: absolute; left: 0; right: 0; text-align: center;
    font-size: 18px; letter-spacing: 0.8px;
  }
  .signature--logo .brand-panel__url { top: 164px; }
  .signature--wordmark .brand-panel__url { top: 164px; }
  .social { position: absolute; left: 130px; top: 250px; display: flex; gap: 36px; }
  .social__dot {
    width: 24px; height: 24px; border-radius: 50%; background: var(--white);
  }
</style>
</head>
<body>
<div class="canvas">

  <section class="signature signature--logo">
    <div class="contact">
      <div class="contact__name">Martin Ellery</div>
      <div class="contact__role">General Manager</div>
      <div class="contact__row contact__row--email">
        <svg class="contact__icon" viewBox="0 0 22 22" aria-hidden="true">
          <rect x="1" y="5" width="20" height="13" fill="var(--accent)"/>
          <path d="M1 5 L11 13 L21 5 M1 18 L8 11 M21 18 L14 11" stroke="#fff" stroke-width="1.4" fill="none"/>
        </svg>
        martin@gainvault.com
      </div>
      <div class="contact__row contact__row--phone">
        <svg class="contact__icon" viewBox="0 0 24 24" aria-hidden="true">
          <path fill="var(--accent)" d="M6.6 10.8a15.1 15.1 0 0 0 6.6 6.6l2.2-2.2c.3-.3.7-.4 1-.2 1.1.4 2.3.6 3.6.6.6 0 1 .4 1 1V20c0 .6-.4 1-1 1A17 17 0 0 1 3 4c0-.6.4-1 1-1h3.5c.6 0 1 .4 1 1 0 1.3.2 2.5.6 3.6.1.3 0 .7-.2 1l-2.3 2.2z"/>
        </svg>
        001 240 518 7729
      </div>
    </div>
    <div class="divider"></div>
    <div class="brand-panel">
      <div class="brand-panel__name">gainvault</div>
      <div class="brand-panel__url">www.gainvault.com</div>
      <div class="social" aria-label="Social profiles">
        <span class="social__dot"></span><span class="social__dot"></span><span class="social__dot"></span>
      </div>
    </div>
  </section>

  <section class="signature signature--wordmark">
    <div class="contact">
      <div class="contact__name">Martin Ellery</div>
      <div class="contact__role">General Manager</div>
      <div class="contact__row contact__row--email">
        <svg class="contact__icon" viewBox="0 0 22 22" aria-hidden="true">
          <rect x="1" y="5" width="20" height="13" fill="var(--accent)"/>
          <path d="M1 5 L11 13 L21 5 M1 18 L8 11 M21 18 L14 11" stroke="#fff" stroke-width="1.4" fill="none"/>
        </svg>
        martin@gainvault.com
      </div>
      <div class="contact__row contact__row--phone">
        <svg class="contact__icon" viewBox="0 0 24 24" aria-hidden="true">
          <path fill="var(--accent)" d="M6.6 10.8a15.1 15.1 0 0 0 6.6 6.6l2.2-2.2c.3-.3.7-.4 1-.2 1.1.4 2.3.6 3.6.6.6 0 1 .4 1 1V20c0 .6-.4 1-1 1A17 17 0 0 1 3 4c0-.6.4-1 1-1h3.5c.6 0 1 .4 1 1 0 1.3.2 2.5.6 3.6.1.3 0 .7-.2 1l-2.3 2.2z"/>
        </svg>
        001 240 518 7729
      </div>
    </div>
    <div class="divider"></div>
    <div class="brand-panel">
      <div class="brand-panel__name">GAINVAULT</div>
      <div class="brand-panel__url">www.gainvault.com</div>
      <div class="social" aria-label="Social profiles">
        <span class="social__dot"></span><span class="social__dot"></span><span class="social__dot"></span>
      </div>
    </div>
  </section>

</div>
</body>
</html>
```